Sports Therapy and Personal Training

I need a business card design for a new business based in Toronto called "Holbrin Athletics" I am a sports therapist as well as a strength and conditioning coach, therefore I work mainly with high level athletes and physically active people. I am starting my own therapy/training business. The services I will be offering include fitness consultation, personal training, athlete assessments, and rehabilitation therapy. These services will be delivered in peoples homes and/or a facility in which I rent space.

The final design should communicate "high-end" and "quality"

Target Market(s)

athletes and physically active people

Industry/Entity Type

Fitness

Requirements
Must have
• 1. The business logo - files attached

2. my name and credentials

Derek Falloway - CAT(C), CK, CSCS,

Certified Athletic Therapist
Strength and Conditioning Specialist

3. website - www.holbrinathletics.example

4. email address - derek@holbrinathletics.example

5. phone number

```html
<!DOCTYPE html>
<html lang="en">
<head>
<meta charset="utf-8">
<title>Holbrin Athletics – Business Card</title>
<link rel="stylesheet" href="https://fonts.googleapis.com/css2?family=Russo+One&family=Open+Sans:wght@700&display=swap">
<style>
  :root {
    --card-bg: #ffffff;
    --panel-top: #ffffff;
    --panel-bottom: #d4d6da;
    --panel-edge: #b9bcc1;
    --accent-red: #e3201f;
    --outline-dark: #2a2a2a;
    --ink: #1e1e1e;
    --brand-ink: #333333;
    --tagline-grey: #8d9096;
    --mark-tint: rgba(150, 150, 155, 0.18);
  }
  html, body {
    margin: 0;
    padding: 0;
    overflow: hidden;
    background: var(--card-bg);
  }
  .card {
    position: relative;
    width: 1200px;
    height: 733px;
    background: var(--card-bg);
    overflow: hidden;
    font-family: "Open Sans", Verdana, sans-serif;
    color: var(--ink);
  }
  .info-panel {
    position: absolute;
    left: 33px;
    top: 160px;
    width: 1145px;
    height: 440px;
    border-radius: 66px;
    border: 2px solid var(--panel-edge);
    background: linear-gradient(180deg, var(--panel-top) 0%, #eef0f2 45%, var(--panel-bottom) 100%);
    box-sizing: border-box;
  }
  .backdrop-mark {
    position: absolute;
    left: 420px;
    top: 40px;
    width: 360px;
    height: 360px;
    border-radius: 50%;
    background: var(--mark-tint);
  }
  .holder-name {
    position: absolute;
    left: 0;
    width: 1200px;
    top: 58px;
    margin: 0;
    text-align: center;
    font-family: "Russo One", sans-serif;
    font-weight: 400;
    font-size: 66px;
    letter-spacing: 3px;
    color: var(--accent-red);
    -webkit-text-stroke: 2px var(--outline-dark);
    text-shadow: 2px 3px 3px rgba(0,0,0,0.35);
  }
  .credentials {
    position: absolute;
    left: 73px;
    top: 196px;
    margin: 0;
    font-size: 29px;
    line-height: 38px;
    font-weight: 700;
  }
  .credentials span { display: block; }
  .contact-list {
    position: absolute;
    left: 150px;
    top: 467px;
    margin: 0;
    font-size: 28px;
    line-height: 39px;
    font-weight: 700;
    display: grid;
    grid-template-columns: 230px auto;
  }
  .contact-list dt { text-align: right; padding-right: 10px; }
  .contact-list dd { margin: 0; }
  .brand-name {
    position: absolute;
    left: 0;
    width: 1200px;
    top: 620px;
    margin: 0;
    text-align: center;
    font-family: "Russo One", sans-serif;
    font-size: 66px;
    letter-spacing: 4px;
    color: var(--brand-ink);
  }
  .brand-tagline {
    position: absolute;
    left: 0;
    width: 1200px;
    top: 694px;
    margin: 0;
    text-align: center;
    font-family: "Russo One", sans-serif;
    font-size: 24px;
    letter-spacing: 3.5px;
    color: var(--tagline-grey);
  }
</style>
</head>
<body>
  <div class="card">
    <div class="info-panel">
      <div class="backdrop-mark" aria-hidden="true"></div>
    </div>

    <h1 class="holder-name">DEREK FALLOWAY</h1>

    <p class="credentials">
      <span>CAT(C), CK, CSCS</span>
      <span>Certified Athletic Therapist</span>
      <span>Strength and Conditioning Specialist</span>
    </p>

    <dl class="contact-list">
      <dt>Visit :</dt><dd>www.holbrinathletics.example</dd>
      <dt>E - Mail :</dt><dd>derek@holbrinathletics.example</dd>
      <dt>Phone :</dt><dd>000 000 000</dd>
    </dl>

    <p class="brand-name">HOLBRIN ATHLETICS</p>
    <p class="brand-tagline">SPORTS MEDICINE • STRENGTH AND CONDITIONING</p>
  </div>
</body>
</html>
```